Poster design for a company operating care homes in the UK showcasing our core values

We need a poster to display in our care homes showcasing our new core values:

Purpose
We are driven by a clear understanding of why we do what we do: to enrich lives, honour legacies and make a meaningful difference every day, for our residents, their families, our colleagues and our community.

Excellence
We hold ourselves to the highest standards, delivering exceptional care and creating an environment where both residents and staff can thrive.

Openness
We build trust through honest, respectful communication, welcoming feedback, sharing ideas, and embracing change as a path to continuous growth.

Passion
We are passionate about delivering exceptional care. We take pride in what we do and in making a real difference in people’s lives.

Learning
We are committed to personal and professional growth; empowering each other through ongoing development, reflection, and shared knowledge.

Empathy
We actively listen and seek to understand before being understood, recognising the unique stories, feelings, and needs of others.

I have attached a small graphic that we would like you try to incorporate, in addition to our company logo. Please theme the rest of the poster around our company colours.

```html
<!DOCTYPE html>
<html lang="en">
<head>
<meta charset="UTF-8">
<title>Core Values Poster – Meridale</title>
<link rel="stylesheet" href="https://fonts.googleapis.com/css2?family=Lexend:wght@400;700&family=Montserrat:wght@800&display=swap">
<style>
  :root {
    --navy: #2f4a6b;
    --navy-deep: #243a56;
    --peach: #e9a27f;
    --white: #ffffff;
    --ink: #1e2633;
  }
  * { margin: 0; padding: 0; box-sizing: border-box; }
  html, body { width: 1085px; height: 1200px; overflow: hidden; background: var(--white); }
  .poster { position: relative; width: 1085px; height: 1200px; overflow: hidden; background: var(--white); font-family: "Lexend", sans-serif; }
  .poster-art { position: absolute; inset: 0; }
  .badge-letter { font-family: "Montserrat", sans-serif; font-weight: 800; font-size: 86px; fill: var(--peach); }
  .title-vertical {
    position: absolute; left: 125px; top: 530px;
    transform: translate(-50%, -50%) rotate(-90deg);
    font-family: "Montserrat", sans-serif; font-weight: 800; font-size: 110px;
    letter-spacing: 2px; color: var(--white); white-space: nowrap; line-height: 1;
  }
  .brand-name {
    position: absolute; left: 62px; top: 1070px;
    font-family: "Lexend", sans-serif; font-weight: 400; font-size: 44px;
    color: var(--white); letter-spacing: 1px; line-height: 1;
  }
  .value { position: absolute; }
  .value-title { font-weight: 700; font-size: 46px; color: var(--navy); line-height: 1.05; margin-bottom: 10px; letter-spacing: -0.5px; }
  .value-text { font-weight: 400; font-size: 17px; line-height: 1.38; color: var(--ink); }
</style>
</head>
<body>
<main class="poster">
  <svg class="poster-art" width="1085" height="1200" viewBox="0 0 1085 1200" aria-hidden="true">
    <defs>
      <linearGradient id="panelShade" x1="0" x2="1" y1="0" y2="0">
        <stop offset="0.55" stop-color="#2f4a6b"/>
        <stop offset="1" stop-color="#243a56"/>
      </linearGradient>
      <filter id="badgeShadow" x="-20%" y="-20%" width="140%" height="140%">
        <feDropShadow dx="0" dy="2" stdDeviation="3" flood-color="#000" flood-opacity="0.25"/>
      </filter>
    </defs>

    <polygon class="navy-panel" points="0,0 270,0 600,1200 0,1200" fill="url(#panelShade)"/>

    <g class="dividers" stroke="#2f4a6b" stroke-width="1.5">
      <line x1="400" y1="240" x2="950" y2="240"/>
      <line x1="450" y1="420" x2="975" y2="420"/>
      <line x1="500" y1="600" x2="1000" y2="600"/>
      <line x1="550" y1="780" x2="1025" y2="780"/>
      <line x1="600" y1="960" x2="1048" y2="960"/>
    </g>
    <g class="divider-dots" fill="#e9a27f">
      <circle cx="964" cy="240" r="8"/>
      <circle cx="989" cy="420" r="8"/>
      <circle cx="1014" cy="600" r="8"/>
      <circle cx="1039" cy="780" r="8"/>
      <circle cx="1062" cy="960" r="8"/>
    </g>

    <g class="badges">
      <g transform="translate(340,150)">
        <circle r="88" fill="#fff" filter="url(#badgeShadow)"/>
        <circle r="74" fill="none" stroke="#e9a27f" stroke-width="7"/>
        <circle r="63" fill="none" stroke="#e9a27f" stroke-width="2.5"/>
        <text class="badge-letter" text-anchor="middle" y="30">P</text>
      </g>
      <g transform="translate(390,330)">
        <circle r="88" fill="#fff" filter="url(#badgeShadow)"/>
        <circle r="74" fill="none" stroke="#e9a27f" stroke-width="7"/>
        <circle r="63" fill="none" stroke="#e9a27f" stroke-width="2.5"/>
        <text class="badge-letter" text-anchor="middle" y="30">E</text>
      </g>
      <g transform="translate(440,510)">
        <circle r="88" fill="#fff" filter="url(#badgeShadow)"/>
        <circle r="74" fill="none" stroke="#e9a27f" stroke-width="7"/>
        <circle r="63" fill="none" stroke="#e9a27f" stroke-width="2.5"/>
        <text class="badge-letter" text-anchor="middle" y="30">O</text>
      </g>
      <g transform="translate(490,690)">
        <circle r="88" fill="#fff" filter="url(#badgeShadow)"/>
        <circle r="74" fill="none" stroke="#e9a27f" stroke-width="7"/>
        <circle r="63" fill="none" stroke="#e9a27f" stroke-width="2.5"/>
        <text class="badge-letter" text-anchor="middle" y="30">P</text>
      </g>
      <g transform="translate(540,870)">
        <circle r="88" fill="#fff" filter="url(#badgeShadow)"/>
        <circle r="74" fill="none" stroke="#e9a27f" stroke-width="7"/>
        <circle r="63" fill="none" stroke="#e9a27f" stroke-width="2.5"/>
        <text class="badge-letter" text-anchor="middle" y="30">L</text>
      </g>
      <g transform="translate(590,1050)">
        <circle r="88" fill="#fff" filter="url(#badgeShadow)"/>
        <circle r="74" fill="none" stroke="#e9a27f" stroke-width="7"/>
        <circle r="63" fill="none" stroke="#e9a27f" stroke-width="2.5"/>
        <text class="badge-letter" text-anchor="middle" y="30">E</text>
      </g>
    </g>
  </svg>

  <h1 class="title-vertical">CORE VALUES</h1>
  <div class="brand-name">MERIDALE</div>

  <section class="value" style="left:452px; top:72px; width:480px;">
    <h2 class="value-title">Purpose</h2>
    <p class="value-text">We are driven by a clear understanding of why we do what we do: to enrich lives, honour legacies and make a meaningful difference every day, for our residents, their families, our colleagues and our community.</p>
  </section>

  <section class="value" style="left:502px; top:262px; width:470px;">
    <h2 class="value-title">Excellence</h2>
    <p class="value-text">We hold ourselves to the highest standards, delivering exceptional care and creating an environment where both residents and staff can thrive.</p>
  </section>

  <section class="value" style="left:552px; top:440px; width:440px;">
    <h2 class="value-title">Openness</h2>
    <p class="value-text">We build trust through honest, respectful communication, welcoming feedback, sharing ideas, and embracing change as a path to continuous growth.</p>
  </section>

  <section class="value" style="left:602px; top:620px; width:400px;">
    <h2 class="value-title">Passion</h2>
    <p class="value-text">We are passionate about delivering exceptional care. We take pride in what we do and in making a real difference in people’s lives.</p>
  </section>

  <section class="value" style="left:652px; top:800px; width:390px;">
    <h2 class="value-title">Learning</h2>
    <p class="value-text">We are committed to personal and professional growth; empowering each other through ongoing development, reflection, and shared knowledge.</p>
  </section>

  <section class="value" style="left:702px; top:978px; width:360px;">
    <h2 class="value-title">Empathy</h2>
    <p class="value-text">We actively listen and seek to understand before being understood, recognising the unique stories, feelings, and needs of others.</p>
  </section>
</main>
</body>
</html>
```